Postcard Design

I am promoting a local school tax levy increase. I need a post card that helps market this. I saw a nice one online that someone did and I'd like something similar. I am attaching a picture of it.
Our election is April 7, 2015 and we want people to vote YES on it!
My bullet points will be: Our Children Our District Our Future
Our colors are Kelly Green and Canary but it is not mandatory that the postcards be those colors. I really like the image I sent you.
We also need to have the name of the ballot measure in smaller print under the date on the side which is: "Proposition Cedar Hollow East High School"
We also need it to say: "Advertisement paid for by the Cedar Hollow East High School Election Committee, Marla Keefe Treasurer.
For the back, you can put our name, address, and a picture of our proposed school which is image #2. You can also put: Call Doug Halvorsen @ 417-555-0187 for more information or to register for an upcoming Q&A forum.
Our name/Address is: Cedar Hollow East High School Election Committee
2756 County Road 3315
Larkdale, MO 65712
You can also include the chatterbook symbol on our card as we are on chatterbook and can include our web address as well which is: www.cedarholloweasthigh.com

Please spell check everything!

Please send me your ideas. I will need postage and address which I will provide once the proof is approved.
Thanks, Doug Halvorsen 417-555-0187

```html
<!DOCTYPE html>
<html lang="en">
<head>
<meta charset="utf-8">
<title>Vote Yes Postcard – Cedar Hollow East High School</title>
<link rel="stylesheet" href="https://fonts.googleapis.com/css2?family=Oswald:wght@700&family=Questrial&family=Open+Sans:wght@400;600;700&display=swap">
<style>
  :root {
    --stage: #ebeceb;
    --kelly: #a2cb3f;
    --canary: #fff200;
    --ink: #2d2b2b;
    --white: #ffffff;
    --back-tint: #e8f2d0;
    --rule: #9aa3a0;
    --muted: #a9aeae;
    --shadow: rgba(0,0,0,0.12);
  }
  * { margin: 0; padding: 0; box-sizing: border-box; }
  html, body { width: 780px; height: 1200px; overflow: hidden; }
  body { background: var(--stage); position: relative; font-family: "Open Sans", sans-serif; color: var(--ink); }

  .card { position: absolute; box-shadow: 0 1px 4px var(--shadow); }

  /* Front */
  .card-front { left: 61px; top: 46px; width: 661px; height: 511px; background: var(--kelly); overflow: hidden; }
  .front-art { position: absolute; left: 0; top: 0; }
  .slogan-row { position: absolute; left: 0; top: 446px; width: 661px; display: flex; font-family: "Questrial", sans-serif; font-size: 24px; color: var(--ink); }
  .slogan { position: absolute; white-space: nowrap; }

  /* Back */
  .card-back { left: 58px; top: 629px; width: 662px; height: 510px; background: var(--back-tint); }
  .committee-name { position: absolute; left: 22px; top: 52px; font-weight: 700; font-size: 14px; }
  .committee-address { position: absolute; left: 22px; top: 83px; font-size: 15.5px; }
  .stamp-box { position: absolute; left: 483px; top: 29px; }
  .info-panel { position: absolute; left: 1px; top: 130px; width: 357px; height: 299px; background: var(--kelly); }
  .web-bar { height: 22px; background: var(--canary); text-align: center; font-size: 14px; line-height: 22px; }
  .school-photo { height: 136px; background: linear-gradient(180deg, #6d9ed6 0%, #a9c8e8 35%, #b8b4a8 55%, #8a7a62 70%, #a7ad9f 85%, #c9ccc6 100%); }
  .contact-note { position: absolute; left: 59px; top: 176px; font-size: 14px; line-height: 19px; }
  .contact-note strong { font-weight: 700; }
  .phone-icon { display: inline-block; vertical-align: -2px; margin-left: 3px; }
  .social { position: absolute; left: 62px; top: 244px; display: flex; align-items: center; gap: 6px; font-size: 14px; }
  .social-mark { width: 28px; height: 28px; background: #3b5ea8; border-radius: 4px; }
  .address-lines { position: absolute; left: 369px; top: 224px; width: 276px; }
  .address-line { height: 1px; background: var(--rule); margin-bottom: 30px; }
  .barcode-label { position: absolute; left: 310px; top: 466px; font-size: 16px; color: var(--muted); }
</style>
</head>
<body>

<section class="card card-front" aria-label="Postcard front">
  <svg class="front-art" width="661" height="511" viewBox="0 0 661 511">
    <!-- tick badge -->
    <circle cx="132" cy="231" r="101" fill="var(--ink)"/>
    <circle cx="132" cy="231" r="88" fill="none" stroke="var(--white)" stroke-width="5"/>
    <path d="M68 233 L110 275 L196 186" fill="none" stroke="var(--white)" stroke-width="24" stroke-linecap="square"/>
    <!-- headline -->
    <text x="244" y="208" font-family="Oswald, sans-serif" font-weight="700" font-size="80" fill="var(--ink)" textLength="180" lengthAdjust="spacingAndGlyphs">VOTE</text>
    <text x="244" y="344" font-family="Oswald, sans-serif" font-weight="700" font-size="138" fill="var(--ink)" stroke="var(--white)" stroke-width="3" paint-order="stroke" textLength="186" lengthAdjust="spacingAndGlyphs">YES</text>
    <line x1="450" y1="144" x2="450" y2="349" stroke="var(--ink)" stroke-width="2"/>
    <!-- date -->
    <text transform="translate(503 315) rotate(-90)" font-family="Questrial, sans-serif" font-size="42" fill="var(--ink)">APRIL <tspan font-family="Oswald, sans-serif" font-weight="700">7</tspan></text>
    <text transform="translate(548 293) rotate(-90)" font-family="Questrial, sans-serif" font-size="40" fill="var(--ink)">2015</text>
    <!-- ballot measure -->
    <text transform="translate(591 416) rotate(-90)" font-family="Questrial, sans-serif" font-size="16.5" fill="var(--ink)" textLength="370" lengthAdjust="spacingAndGlyphs">Proposition Cedar Hollow East High School</text>
    <text transform="translate(623 417) rotate(-90)" font-family="Questrial, sans-serif" font-size="11.5" fill="var(--ink)" textLength="370" lengthAdjust="spacingAndGlyphs">Advertisement paid for by the Cedar Hollow East High School</text>
    <text transform="translate(639 383) rotate(-90)" font-family="Questrial, sans-serif" font-size="11.5" fill="var(--ink)">Election Committee, Marla Keefe Treasurer</text>
    <!-- tabbed canary band -->
    <path d="M0 434 H22 Q40 434 42 450 Q44 434 60 434 H226 Q244 434 246 450 Q248 434 264 434 H424 Q442 434 444 450 Q446 434 462 434 H620 Q638 434 640 450 Q642 434 658 434 H661 V511 H0 Z" fill="var(--canary)" stroke="var(--ink)" stroke-width="1"/>
    <text x="57" y="471" font-family="Questrial, sans-serif" font-size="24" fill="var(--ink)">OUR CHILDREN</text>
    <text x="271" y="471" font-family="Questrial, sans-serif" font-size="24" fill="var(--ink)">OUR DISTRICT</text>
    <text x="466" y="471" font-family="Questrial, sans-serif" font-size="24" fill="var(--ink)">OUR FUTURE</text>
  </svg>
</section>

<section class="card card-back" aria-label="Postcard back">
  <p class="committee-name">Cedar Hollow East High School Election Committee</p>
  <p class="committee-address">2756 County Road 3315 Larkdale, MO 65712</p>

  <svg class="stamp-box" width="146" height="110" viewBox="0 0 146 110" aria-label="Postage stamp area">
    <rect x="3" y="3" width="140" height="104" fill="#f8fbf0" stroke="#9a9a9a" stroke-width="1.2" stroke-dasharray="3 2"/>
  </svg>

  <div class="info-panel">
    <div class="web-bar">www.cedarholloweasthigh.com</div>
    <div class="school-photo" role="img" aria-label="Rendering of the proposed high school building with lawn and driveway"></div>
    <p class="contact-note">Call&nbsp; <strong>Doug Halvorsen</strong><svg class="phone-icon" width="11" height="14" viewBox="0 0 11 14"><path d="M3 1 L5 4 L3.5 5.5 Q4.5 8.5 6.5 10 L8 8.8 L10.5 11 L8.5 13 Q2 11 1 3 Z" fill="var(--ink)"/></svg><strong>417-555-0187</strong><br>for more information or to register<br>for an upcoming Q&amp;A forum.</p>
    <div class="social"><span class="social-mark"></span><span>chatterbook</span></div>
  </div>

  <div class="address-lines">
    <div class="address-line"></div>
    <div class="address-line"></div>
    <div class="address-line"></div>
    <div class="address-line"></div>
    <div class="address-line"></div>
  </div>

  <p class="barcode-label">Barcode Area</p>
</section>

</body>
</html>
```